Banner & also another minor digital image for an Online Academic Journal

A direct example of what I need can be found in this webpage: http://papers.tbhu-archive.org/qrvt/
(Please see attached files, "sAMPLE", and "sAMPLE 2", so you can see what I mean.)
This link (http://papers.tbhu-archive.org/qrvt/) is for an existing ONLINE ACADEMIC JOURNAL at the Thornbury Hill University.
It will help for you to be acquainted with the format of Online Academic Journals.
You will find that there is a banner on top as well as a digital image of a journal/book cover on the right.
I need a
(1) banner and
a (2) digital journal/book cover
for a website for an ONLINE ACADEMIC JOURNAL.
I am looking for a serious, professional, elegant design.
There will not be a print version. Only web-based online publication. No coding needed, only PSD, JPG/PNG and PDF.
1) We use PelloWave (http://archives.pellowave.com/repository-software/journals/) for the digital image of the journal/book cover layout. Link shows the general layout of the journal website.
2) For the digital image of the journal/book cover and also the banner,
Name of the journal is....
"Lumen: A Quarterly of Civic Ethics and Recovery Work"
Only this text will be used and applied to both banner and cover.
***The color associated with the theme of dignity is purple
****You could also add the color red.
*****I don't want the design to be garish, but accents in red might represent
the sexual exploitation and violence in the title.
3) Attached "sAmple 2" file is a basic design for the digital image of the journal/book cover from PelloWave. I am looking for something more elegant and professional looking. Your creativity is encouraged. I am open to receiving your interpretation.
Target Market(s)
Academics & Community Professionals
Industry/Entity Type
Non Profit
Contact Information for Business Card
Match journal design

```html
<!DOCTYPE html>
<html lang="en">
<head>
<meta charset="utf-8">
<title>Lumen – Banner and Cover</title>
<link rel="stylesheet" href="https://fonts.googleapis.com/css2?family=Cinzel:wght@400&family=Arimo:wght@400&display=swap">
<style>
  :root {
    --page-bg: #ffffff;
    --violet: #866aab;
    --violet-deep: #604b84;
    --violet-mid: #6f5896;
    --accent-red: #e84a5f;
    --text-light: #ffffff;
  }
  * { margin: 0; padding: 0; box-sizing: border-box; }
  html, body {
    width: 919px;
    height: 1200px;
    overflow: hidden;
    background: var(--page-bg);
  }
  .canvas {
    position: relative;
    width: 919px;
    height: 1200px;
  }
  .journal-banner {
    position: absolute;
    left: 88px;
    top: 295px;
    width: 785px;
    height: 98px;
    background: var(--violet);
    overflow: hidden;
  }
  .journal-cover {
    position: absolute;
    left: 334px;
    top: 512px;
    width: 306px;
    height: 443px;
    background: var(--violet);
    overflow: hidden;
  }
  .artwork {
    position: absolute;
    inset: 0;
  }
  .journal-title {
    position: absolute;
    font-family: "Cinzel", serif;
    font-weight: 400;
    color: var(--text-light);
    letter-spacing: 1px;
    line-height: 1;
  }
  .journal-subtitle {
    position: absolute;
    font-family: "Arimo", Arial, sans-serif;
    font-weight: 400;
    color: var(--text-light);
    text-align: right;
    white-space: nowrap;
  }
  .journal-banner .journal-title {
    left: 69px;
    top: 30px;
    font-size: 32px;
  }
  .journal-banner .journal-subtitle {
    right: 70px;
    top: 33px;
    font-size: 16.5px;
    line-height: 19px;
  }
  .journal-cover .journal-title {
    left: 0;
    right: 0;
    top: 81px;
    text-align: center;
    font-size: 38px;
  }
  .subtitle-band {
    position: absolute;
    left: 0;
    top: 153px;
    width: 306px;
    height: 64px;
    background: var(--violet-deep);
  }
  .journal-cover .journal-subtitle {
    right: 29px;
    top: 12px;
    font-size: 16px;
    line-height: 21px;
  }
</style>
</head>
<body>
<div class="canvas">

  <section class="journal-banner" aria-label="Journal banner">
    <svg class="artwork" width="785" height="98" viewBox="0 0 785 98" aria-hidden="true">
      <path d="M0,84 Q380,100 785,44 L785,98 L0,98 Z" fill="var(--violet-mid)"/>
      <path d="M330,98 Q610,82 785,32 L785,98 Z" fill="var(--violet-deep)"/>
      <path d="M0,74 Q180,84 335,88 L335,91 Q180,88 0,79 Z" fill="var(--accent-red)"/>
    </svg>
    <svg class="artwork" width="785" height="98" viewBox="0 0 785 98" role="img" aria-label="Illustration area: silhouette of an outstretched hand reaching upward">
      <defs>
        <radialGradient id="banner-hand-glow" cx="0.45" cy="0.55" r="0.55">
          <stop offset="0" stop-color="#604b84" stop-opacity="0.75"/>
          <stop offset="1" stop-color="#604b84" stop-opacity="0"/>
        </radialGradient>
      </defs>
      <rect x="255" y="0" width="170" height="98" fill="url(#banner-hand-glow)"/>
    </svg>
    <div class="journal-title">LUMEN</div>
    <div class="journal-subtitle">A Quarterly of Civic Ethics<br>and Recovery Work</div>
  </section>

  <section class="journal-cover" aria-label="Journal cover">
    <svg class="artwork" width="306" height="443" viewBox="0 0 306 443" aria-hidden="true">
      <path d="M0,424 Q175,452 306,346 L306,443 L0,443 Z" fill="var(--violet-deep)"/>
      <path d="M0,410 Q175,446 306,334 L306,352 Q175,456 0,424 Z" fill="var(--accent-red)"/>
    </svg>
    <svg class="artwork" width="306" height="443" viewBox="0 0 306 443" role="img" aria-label="Illustration area: silhouette of an outstretched hand reaching upward">
      <defs>
        <radialGradient id="cover-hand-glow" cx="0.45" cy="0.55" r="0.55">
          <stop offset="0" stop-color="#604b84" stop-opacity="0.75"/>
          <stop offset="1" stop-color="#604b84" stop-opacity="0"/>
        </radialGradient>
      </defs>
      <rect x="20" y="270" width="225" height="173" fill="url(#cover-hand-glow)"/>
    </svg>
    <div class="journal-title">LUMEN</div>
    <div class="subtitle-band">
      <div class="journal-subtitle">A Quarterly of Civic Ethics<br>and Recovery Work</div>
    </div>
  </section>

</div>
</body>
</html>
```